Career Development Skills | Business Card & Logo Design

We are looking for a business card including logo design for a new Sydney based business called 'Your Careerwise'.
We offer a range of services that focus on building the Employability or Employment skills for individuals focusing on job seekers and those interested in building skills required to develop their career. Employability skills are required not only to gain employment, but also to progress within an organisation so as to achieve one's potential.
Target Market(s)
Our client targets include corporates and govt agencies looking to build skills within their current employee base or assist staff in the transition between roles or workplaces.
Industry/Entity Type
Business
Look and feel

```html
<!DOCTYPE html>
<html lang="en">
<head>
<meta charset="utf-8">
<title>Your Careerwise – Business Card</title>
<link rel="stylesheet" href="https://fonts.googleapis.com/css2?family=Pathway+Gothic+One&display=swap">
<style>
  :root {
    --backdrop: #2a2a2c;
    --navy: #0c1480;
    --ink-navy: #1f2c8e;
    --ink-grey: #4f5354;
    --white: #ffffff;
    --card-light-a: #c5d0ce;
    --card-light-b: #fbfbfc;
    --mark-grey-a: #8b8f90;
    --mark-grey-b: #e8eaea;
  }
  * { box-sizing: border-box; margin: 0; padding: 0; }
  html, body {
    width: 1200px; height: 1164px; overflow: hidden;
    background: var(--backdrop);
  }
  .canvas { position: relative; width: 1200px; height: 1164px; }
  .card {
    position: absolute; overflow: hidden;
    font-family: "Pathway Gothic One", "Arial Narrow", sans-serif;
  }
  .card-front {
    left: 96px; top: 116px; width: 701px; height: 427px;
    background: var(--navy);
  }
  .brand {
    position: absolute; left: 190px; top: 292px;
    display: flex; align-items: center; gap: 16px;
  }
  .card-front .brand { left: 94px; top: 176px; }
  .brand-dot {
    width: 44px; height: 44px; border-radius: 50%;
    background: var(--white);
  }
  .brand-name {
    color: var(--white); font-size: 54px; letter-spacing: 3px;
    text-transform: uppercase; line-height: 1;
  }
  .card-back {
    left: 409px; top: 592px; width: 704px; height: 429px;
    background: linear-gradient(120deg, var(--card-light-a) 0%, var(--card-light-b) 75%);
  }
  .back-mark {
    position: absolute; left: 520px; top: 60px;
    width: 280px; height: 280px; border-radius: 50%;
    background: linear-gradient(180deg, var(--mark-grey-a), var(--mark-grey-b));
  }
  .rule {
    position: absolute; left: 155px; top: 98px;
    width: 2px; height: 244px; background: var(--ink-navy);
  }
  .details {
    position: absolute; left: 183px; top: 94px;
    font-size: 17px; line-height: 21px; color: var(--ink-grey);
  }
  .contact { color: var(--ink-navy); margin-bottom: 22px; }
  .address { margin-bottom: 31px; line-height: 21.5px; }
  .phones div { display: flex; gap: 4px; line-height: 23px; }
  .phones .label { color: var(--ink-navy); }
  .phones .dashes { color: var(--ink-navy); letter-spacing: 0; }
</style>
</head>
<body>
<main class="canvas">
  <section class="card card-front" aria-label="Business card front">
    <div class="brand">
      <span class="brand-dot"></span>
      <span class="brand-name">Your Careerwise</span>
    </div>
  </section>

  <section class="card card-back" aria-label="Business card back">
    <div class="back-mark"></div>
    <div class="rule"></div>
    <div class="details">
      <div class="contact">
        <div>Daniel Hartley - Director</div>
        <div>Yourcareerwise.com.au</div>
        <div>Daniel@yourcareerwise.com.au</div>
      </div>
      <div class="address">
        <div>Level 14</div>
        <div>Harbour Point Tower 3</div>
        <div>118&nbsp;&nbsp;&nbsp; Kent Street</div>
        <div>Harbour Point, Sydney 2000</div>
      </div>
      <div class="phones">
        <div><span class="label">Tell</span><span class="dashes">---------------</span><span>(02)&nbsp; 90155420</span></div>
        <div><span class="label">Fax</span><span class="dashes">---------------</span><span>(02)&nbsp; 90155421</span></div>
      </div>
    </div>
  </section>
</main>
</body>
</html>
```